Flyer-Design für Personal Training
Ich bin sehr zufrieden mit der Arbeit der Designerin. Auf Änderungswünsche wurde immer schnell eingegangen und ich habe viele tolle Inputs erhalten. Ich werde definitiv wieder mit ihr arbeiten.
Zielgruppe
Ich gebe Personal Training und Outdoor Gruppen-Training. Meine Kunden sind jung bis alt(20-50), mändlich und weiblich. Das Personal Training ist eher im Hochpreis Segment das OGT nicht.
Aufgabenstellung
Der Flyer soll die 3 athletikfaktoren: Kraft, Schnelligkeit und Ausdauer beinhalten. Farblich soll er meinem Logo angepasst sein. Der Flyer wird in Arztpraxen und Physiotherapien aufgelegt und sollte in diese Umgebung passen.
Falzflyer A6: Front Logo, inen links der Trainer und Angebot, inen rechts die beiden Trainings. Back Kontakt und map.
Ich werde die Flyer bei Druckmalo drucken lassen - bitte die druckvorlagen beachten (seitenränder usw.)
Im pdf Flyer sind die Texte.
Bitte einen QR für Zulo und ev. noch einen für die Kontaktdaten in das Layout einbauen.

```html
<!DOCTYPE html>
<html lang="de">
<head>
<meta charset="utf-8">
<title>Falzflyer Personal Training – Tempo &amp; Vital</title>
<link rel="stylesheet" href="https://fonts.googleapis.com/css2?family=Cabin:wght@400;500&family=Montserrat:wght@500;700&family=Rubik:ital,wght@1,900&display=swap">
<style>
  :root{
    --navy:#1f3e70;
    --navy-line:#17315a;
    --mist:#b9cbdb;
    --mist-light:#d3dee7;
    --paper:#ffffff;
    --ink:#1d1d1f;
    --photo-light:#eef1f4;
    --photo-mid:#d4dbe2;
  }
  *{margin:0;padding:0;box-sizing:border-box}
  html,body{width:837px;height:1200px;overflow:hidden;background:var(--paper)}
  body{position:relative;font-family:"Cabin",sans-serif;color:var(--ink)}

  .panel{position:absolute;left:43px;width:749px;overflow:hidden}

  /* Outside spread */
  .outside{top:43px;height:537px;background:var(--navy)}
  .outside__fold-frame{position:absolute;left:12px;top:13px;width:363px;height:511px;border:1px solid var(--navy-line)}
  .back-contact{position:absolute;left:12px;top:225px;width:363px;text-align:center;color:var(--paper)}
  .social{display:flex;justify-content:center;gap:10px;font-size:10px;letter-spacing:.04em}
  .social span{display:inline-flex;align-items:center;gap:4px}
  .social span::before{content:"";width:9px;height:9px;border-radius:50%;background:currentColor}
  .back-contact .rule{width:154px;height:1px;background:var(--paper);margin:10px auto 7px;opacity:.9}
  .back-contact p{font-size:11.5px;line-height:18.5px;font-weight:400}

  .brand{position:absolute;left:420px;top:230px;width:329px;text-align:center;color:var(--paper)}
  .brand__mark{width:34px;height:34px;border-radius:50%;background:var(--paper);margin:0 auto 20px}
  .brand__name{font-family:"Montserrat",sans-serif;font-weight:700;font-size:13.5px;letter-spacing:.2em}
  .brand__sub{display:flex;align-items:center;justify-content:center;gap:6px;margin-top:4px;font-family:"Montserrat",sans-serif;font-weight:500;font-size:8px;letter-spacing:.22em}
  .brand__sub::before,.brand__sub::after{content:"";width:52px;height:1px;background:var(--paper)}

  /* Inside spread */
  .inside{top:619px;height:535px;background:var(--photo-light)}
  .inside svg.backdrop{position:absolute;inset:0}

  .trainer-photo{position:absolute;left:60px;top:111px;width:164px;height:255px;border-radius:60px 60px 0 0;background:linear-gradient(180deg,#3a3f4a 0%,#1b1e26 100%)}

  .headline{font-family:"Rubik",sans-serif;font-style:italic;font-weight:900;text-transform:uppercase;color:var(--paper);
    text-shadow:1.5px 1.5px 0 var(--navy),-1px -1px 0 var(--navy),1px -1px 0 var(--navy),-1px 1px 0 var(--navy)}

  .offer{position:absolute;right:408px;top:40px;text-align:right}
  .offer .headline{font-size:21px;line-height:24px}
  .offer ul{list-style:none;font-size:14px;line-height:17.6px;margin-top:2px}

  .about{position:absolute;left:39px;top:346px;width:310px}
  .about .headline{font-size:27px;line-height:30px}
  .about p{font-size:11px;line-height:14.7px;margin-top:2px}

  .training{position:absolute;left:386px}
  .training .headline{font-size:16px;line-height:17.5px}
  .training .rule{height:1px;background:var(--ink);margin:3px 0 8px -2px}
  .training p{font-size:10px;line-height:13.1px}
  .training--outdoor{top:53px;width:216px}
  .training--outdoor .rule{width:216px}
  .training--personal{top:309px;width:214px}
  .training--personal .rule{width:200px}

  .round-photo{position:absolute;border-radius:50%;border:2px solid var(--paper)}
  .round-photo--group{left:559px;top:104px;width:126px;height:126px;background:linear-gradient(180deg,#4d6a44 0%,#6f8a56 55%,#8b6b5a 100%)}
  .round-photo--studio{left:599px;top:312px;width:126px;height:126px;background:linear-gradient(180deg,#f2f3f5 0%,#9aa0a6 60%,#2b2d31 100%)}

  .inside-contact{position:absolute;right:25px;top:452px;text-align:right;color:#2a3b52}
  .inside-contact .social{justify-content:flex-end;color:var(--paper);margin-bottom:4px}
  .inside-contact p{font-size:11px;line-height:15px}
</style>
</head>
<body>

<section class="panel outside">
  <div class="outside__fold-frame"></div>
  <div class="back-contact">
    <div class="social"><span>Fasto</span><span>Zulo</span></div>
    <div class="rule"></div>
    <p>Telefon:0123 4567890</p>
    <p>E-Mail: kontakt@jonaswehrli.de</p>
    <p>Web: www.jonaswehrli.de</p>
  </div>
  <div class="brand">
    <div class="brand__mark"></div>
    <div class="brand__name">TEMPO &amp; VITAL</div>
    <div class="brand__sub">JONAS WEHRLI</div>
  </div>
</section>

<section class="panel inside">
  <svg class="backdrop" width="749" height="535" viewBox="0 0 749 535">
    <defs>
      <linearGradient id="photoLeft" x1="0" y1="0" x2="0" y2="1">
        <stop offset="0" stop-color="#f1f2f3"/><stop offset="1" stop-color="#c9cdd2"/>
      </linearGradient>
      <linearGradient id="photoRight" x1="0" y1="0" x2="0" y2="1">
        <stop offset="0" stop-color="#f3f4f6"/><stop offset="1" stop-color="#d5d8dc"/>
      </linearGradient>
    </defs>
    <rect x="0" y="0" width="375" height="535" fill="url(#photoLeft)" role="img" aria-label="Hintergrundfoto: Trainierende mit Kurzhantel im Ausfallschritt"/>
    <rect x="375" y="0" width="374" height="535" fill="url(#photoRight)" role="img" aria-label="Hintergrundfoto: privates Fitnessstudio mit Hantelablage"/>
    <polygon points="185,0 564,0 375,190" fill="var(--mist)" opacity=".85"/>
    <path d="M0,350 Q90,380 170,360 L375,330 L375,535 L0,535 Z" fill="var(--mist-light)" opacity=".8"/>
    <path d="M0,4 L133,137 Q230,225 222,290 Q212,345 150,352 Q60,360 0,318 Z" fill="var(--navy)"/>
    <polygon points="693,0 749,0 749,125 640,232 612,205" fill="var(--navy)"/>
    <polygon points="749,165 749,195 655,290 640,275" fill="var(--paper)" opacity=".7"/>
    <polygon points="749,196 749,388 690,445 640,330" fill="var(--navy)"/>
  </svg>

  <div class="trainer-photo" role="img" aria-label="Porträtfoto des Trainers mit verschränkten Armen"></div>

  <div class="offer">
    <h2 class="headline">Angebot:</h2>
    <ul>
      <li>Personal Training</li>
      <li>Personal Training Duo</li>
      <li>Athletik Training</li>
      <li>Outdoor Training</li>
    </ul>
  </div>

  <div class="about">
    <h2 class="headline">Wer bin ich:</h2>
    <p>Als ehemaliger Leistungssportler in der Leichtathletik und später im Kickboxen habe ich selbst über 20 Jahre an meiner Kraft, Schnelligkeit und Ausdauer gearbeitet. Als Trainer kann ich nun meine Erfahrungen an Dich weitergeben. Zahlreiche Aus- und Weiterbildungen im Personal Training, Functional Training und im Outdoor Training ermöglichen es mir, Dich professionell zu deinem Ziel zu führen.</p>
  </div>

  <div class="training training--outdoor">
    <h3 class="headline">Outdoor<br>Gruppen-Teilnehmer:</h3>
    <div class="rule"></div>
    <p>Training im Freien mit dem eigenen<br>Körpergewicht mit verschiedenen<br>hilfsmitteln in Gruppen mit max. 10<br>Teilnehmenden, für Einsteigerinnen<br>bis Fortgeschrittene.</p>
  </div>
  <div class="round-photo round-photo--group" role="img" aria-label="Foto: Outdoor-Gruppentraining mit Medizinball auf dem Sportplatz"></div>

  <div class="training training--personal">
    <h3 class="headline">Personal Training:</h3>
    <div class="rule"></div>
    <p>Nach Analyse deiner Fitness/Leistungs-<br>fähigkeiten stelle ich einen individuell auf dich<br>abgestimmten Trainingsplan und betreue dich<br>1:1 in meinem privaten Fitnessstudio, im Freien<br>oder bei dir zuhause.</p>
  </div>
  <div class="round-photo round-photo--studio" role="img" aria-label="Foto: Fitnessstudio mit Kraftstation, Hanteln und Bank"></div>

  <div class="inside-contact">
    <div class="social"><span>Fasto</span><span>Zulo</span></div>
    <p>Telefon:0123 4567890</p>
    <p>E-Mail: kontakt@jonaswehrli.de</p>
    <p>Web: www.jonaswehrli.de</p>
  </div>
</section>

</body>
</html>
```